Business Card for Trivelo, a french tech company

Tech company
New technologies
Serious design
Dark theme

User info :
Name: Florian GASTIER
Position: Co-Founder & CEO
Tel: (+33) 6 52 84 26 07
Email: florian@trivelo.example
Website: www.trivelo.example
Address: 17 rue des Tanneurs 69001 LYON

```html
<!DOCTYPE html>
<html lang="fr">
<head>
<meta charset="utf-8">
<title>Trivelo — Business Card</title>
<link rel="stylesheet" href="https://fonts.googleapis.com/css2?family=Open+Sans:wght@400;600;700&display=swap">
<style>
  :root {
    --stage: #222222;
    --navy-deep: #0f0c3c;
    --navy: #1a1658;
    --navy-mid: #17135a;
    --navy-band: #120f48;
    --teal: #1a7a9e;
    --indigo: #152552;
    --magenta: #e0249a;
    --violet: #8a4fb0;
    --white: #ffffff;
  }
  * { box-sizing: border-box; margin: 0; padding: 0; }
  html, body { width: 1200px; height: 780px; overflow: hidden; }
  body {
    background: var(--stage);
    font-family: "Open Sans", Arial, sans-serif;
    position: relative;
  }
  .card {
    position: absolute;
    top: 125px;
    width: 340px;
    height: 530px;
    border-radius: 22px;
    overflow: hidden;
    box-shadow: 0 10px 28px rgba(0,0,0,0.55);
  }

  /* Front */
  .card--front {
    left: 230px;
    background: linear-gradient(170deg, var(--teal) 0%, var(--indigo) 32%, var(--navy-deep) 68%, var(--navy-deep) 100%);
  }
  .front__wordmark {
    position: absolute;
    left: 50%;
    top: 50%;
    transform: translate(-50%, -50%) rotate(-90deg);
    color: var(--white);
    font-weight: 700;
    font-size: 62px;
    letter-spacing: 6px;
    text-transform: uppercase;
    white-space: nowrap;
  }

  /* Back */
  .card--back { left: 630px; background: var(--navy); }
  .back__bands { position: absolute; inset: 0; }
  .back__brand {
    position: absolute;
    left: 0; top: 0;
    width: 100%; height: 190px;
    background: var(--white);
    display: flex;
    align-items: center;
    justify-content: center;
    gap: 14px;
  }
  .brand__dot {
    width: 26px; height: 26px;
    border-radius: 50%;
    background: var(--magenta);
  }
  .brand__name {
    color: var(--navy-deep);
    font-weight: 700;
    font-size: 44px;
  }
  .back__identity {
    position: absolute;
    top: 212px; left: 0; width: 100%;
    text-align: center;
    color: var(--white);
  }
  .identity__name {
    font-weight: 700;
    font-size: 25px;
    background: linear-gradient(90deg, var(--magenta), var(--violet));
    -webkit-background-clip: text;
    background-clip: text;
    color: transparent;
    line-height: 1.15;
  }
  .identity__role { font-size: 14px; font-weight: 600; margin-top: 2px; }
  .contact__icons {
    display: flex; justify-content: center; gap: 10px;
    margin: 14px 0 8px;
  }
  .contact__icons svg { width: 16px; height: 16px; }
  .contact__line { font-size: 13px; line-height: 1.55; }
  .back__address {
    position: absolute;
    top: 432px; left: 0; width: 100%;
    text-align: center;
    color: var(--white);
    font-size: 13px;
    line-height: 1.45;
  }
  .back__address svg { width: 16px; height: 18px; margin-bottom: 4px; }
</style>
</head>
<body>

<section class="card card--front" aria-label="Recto">
  <span class="front__wordmark">Trivelo</span>
</section>

<section class="card card--back" aria-label="Verso">
  <svg class="back__bands" viewBox="0 0 340 530" preserveAspectRatio="none" aria-hidden="true">
    <defs>
      <filter id="band-shadow" x="-20%" y="-20%" width="140%" height="160%">
        <feDropShadow dx="0" dy="6" stdDeviation="7" flood-color="#05031c" flood-opacity="0.6"/>
      </filter>
    </defs>
    <rect x="0" y="190" width="340" height="340" fill="#1c1860"/>
    <path d="M0 190 H340 V355 Q230 468 40 472 L0 472 Z" fill="#17135a" filter="url(#band-shadow)"/>
    <path d="M0 190 H340 V292 Q255 412 60 410 L0 410 Z" fill="#120f48" filter="url(#band-shadow)"/>
  </svg>

  <div class="back__brand">
    <span class="brand__dot"></span>
    <span class="brand__name">Trivelo</span>
  </div>

  <div class="back__identity">
    <h1 class="identity__name">Florian GASTIER</h1>
    <p class="identity__role">Co-Founder &amp; CEO</p>
    <div class="contact__icons" aria-hidden="true">
      <svg viewBox="0 0 16 16"><path d="M4 1.5l2 3-1.3 1.3a8 8 0 0 0 5.5 5.5L11.5 10l3 2-1 2.5C7 14.5 1.5 9 1.5 2.5z" fill="#fff"/></svg>
      <svg viewBox="0 0 16 16"><rect x="1.5" y="3.5" width="13" height="9" rx="1" fill="none" stroke="#fff" stroke-width="1.4"/><path d="M1.5 4l6.5 5 6.5-5" fill="none" stroke="#fff" stroke-width="1.4"/></svg>
      <svg viewBox="0 0 16 16"><circle cx="8" cy="8" r="6.5" fill="none" stroke="#fff" stroke-width="1.3"/><ellipse cx="8" cy="8" rx="2.8" ry="6.5" fill="none" stroke="#fff" stroke-width="1.1"/><path d="M1.5 8h13" stroke="#fff" stroke-width="1.1"/></svg>
    </div>
    <p class="contact__line">(+33) 6 52 84 26 07</p>
    <p class="contact__line">www.trivelo.example</p>
    <p class="contact__line">florian@trivelo.example</p>
  </div>

  <address class="back__address" style="font-style:normal">
    <svg viewBox="0 0 16 18" aria-hidden="true"><path d="M8 1a5 5 0 0 0-5 5c0 3.5 5 9 5 9s5-5.5 5-9a5 5 0 0 0-5-5z" fill="none" stroke="#fff" stroke-width="1.4"/><circle cx="8" cy="6" r="1.8" fill="#fff"/></svg><br>
    17 rue des Tanneurs<br>69001 LYON
  </address>
</section>

</body>
</html>
```